Quorvix Letter head

Quorvix is a young and energetic software development consultancy. We spend our time working with clients to turn what ever is in their heads in to software.
We are trying to create an image of a high class software boutique who build class leading bespoke solutions.
We need a sharp letter head that looks great on high quality media.
We like bold colours and distinctive design. So show us what you can do.
Industry/Entity Type
Software
Requirements
Must have
- Our company is based in the UK and are requried to have on the paper somewhere the following information:
* Registered company name: Quorvix Ltd
* Registered company number
* VAT registration number
In addition we also want the following:
* An email address
* Telephone number
* Website address
An example of what some pages have in their footer is something like the following:
Quorvix Ltd is registered in England and Wales. Reg. no: 5316274
Registered office: 48 Cobblewick Road, Harlow Essex, CM93TP. Tel: 07712365081
You do not have to use this sentance but please make sure your design incorporates accommodates the requirements for UK based companies

```html
<!DOCTYPE html>
<html lang="en">
<head>
<meta charset="utf-8">
<title>Quorvix Letterhead</title>
<link href="https://fonts.googleapis.com/css2?family=Source+Sans+3:wght@400;600&display=swap" rel="stylesheet">
<style>
  :root {
    --brand-red: #c8202a;
    --deep-red: #8e0f17;
    --bright-red: #e3232b;
    --ink: #3a3a3a;
    --muted: #555555;
    --rule: #b9b9b9;
    --paper: #ffffff;
    --watermark: #f6ebe7;
    --band-grey-light: #d9d9d9;
    --band-grey-dark: #8a8a8a;
  }
  * { margin: 0; padding: 0; box-sizing: border-box; }
  html, body { width: 986px; height: 1200px; overflow: hidden; background: var(--paper); }
  body { font-family: "Source Sans 3", "Myriad Pro", sans-serif; color: var(--ink); }
  .letterhead { position: relative; width: 986px; height: 1200px; background: var(--paper); }

  .brand-name {
    position: absolute; left: 52px; top: 36px;
    font-size: 72px; font-weight: 600; line-height: 1;
    letter-spacing: 1px; color: var(--brand-red);
  }

  .contact-list {
    position: absolute; right: 240px; top: 38px;
    list-style: none; text-align: right;
    font-size: 16.5px; line-height: 24px; color: var(--muted);
  }
  .contact-list li { display: flex; align-items: center; justify-content: flex-end; gap: 7px; }
  .contact-list svg { width: 15px; height: 15px; flex: none; }

  .header-rule {
    position: absolute; left: 762px; top: 40px;
    width: 1px; height: 75px; background: var(--rule);
  }

  .office-address {
    position: absolute; left: 775px; top: 40px;
    font-style: normal; font-size: 16.5px; line-height: 22.5px; color: var(--muted);
  }

  .watermark {
    position: absolute; left: 0; right: 0; top: 540px;
    text-align: center; font-size: 132px; font-weight: 600;
    line-height: 1; letter-spacing: 4px; color: var(--watermark);
  }

  .footer-band { position: absolute; left: 0; bottom: 0; width: 986px; height: 46px; }
  .footer-band svg { position: absolute; inset: 0; }
  .reg-details {
    position: absolute; left: 87px; top: 4px;
    font-size: 14.5px; color: #222; white-space: nowrap;
  }
  .reg-details .divider { font-weight: 600; margin: 0 5px; }
  .registered-entity {
    position: absolute; left: 601px; top: 0; height: 46px;
    display: flex; align-items: center;
    font-size: 16.5px; font-weight: 600; color: #fff; white-space: nowrap;
  }
</style>
</head>
<body>
<main class="letterhead">
  <header>
    <div class="brand-name">Quorvix</div>

    <ul class="contact-list">
      <li>
        <svg viewBox="0 0 16 16" aria-hidden="true"><circle cx="8" cy="8" r="7" fill="none" stroke="var(--brand-red)" stroke-width="1.4"/><path d="M6 4.5c-.8.6-1 1.8-.3 3.3s1.9 2.9 3.3 3.6c.8.4 1.5.2 1.9-.3l-1.3-1.3-.9.5c-.6-.3-1.5-1.3-1.8-2l.5-.9z" fill="var(--brand-red)"/></svg>
        07712365081
      </li>
      <li>
        <svg viewBox="0 0 16 16" aria-hidden="true"><rect x="1" y="4" width="14" height="9" rx="1" fill="var(--brand-red)"/><path d="M1.5 4.5 8 9l6.5-4.5" fill="none" stroke="#fff" stroke-width="1.3"/></svg>
        info@quorvix.com
      </li>
      <li>
        <svg viewBox="0 0 16 16" aria-hidden="true"><g fill="none" stroke="var(--brand-red)" stroke-width="1.2"><circle cx="8" cy="8" r="6.5"/><ellipse cx="8" cy="8" rx="3" ry="6.5"/><path d="M1.5 8h13M2.5 5h11M2.5 11h11"/></g></svg>
        www.quorvix.com
      </li>
    </ul>

    <div class="header-rule"></div>

    <address class="office-address">
      48 Cobblewick Road<br>
      Harlow Essex<br>
      CM93TP
    </address>
  </header>

  <div class="watermark" aria-hidden="true">Quorvix</div>

  <footer class="footer-band">
    <svg viewBox="0 0 986 46" width="986" height="46" aria-hidden="true">
      <defs>
        <linearGradient id="greyBand" x1="0" x2="1" y1="0" y2="0">
          <stop offset="0" stop-color="var(--band-grey-light)"/>
          <stop offset="0.55" stop-color="#c4c4c4"/>
          <stop offset="1" stop-color="var(--band-grey-dark)"/>
        </linearGradient>
        <linearGradient id="redBand" x1="0" x2="1" y1="0" y2="0">
          <stop offset="0" stop-color="var(--bright-red)"/>
          <stop offset="0.5" stop-color="var(--brand-red)"/>
          <stop offset="1" stop-color="var(--deep-red)"/>
        </linearGradient>
      </defs>
      <rect x="0" y="0" width="986" height="46" fill="url(#redBand)"/>
      <polygon points="0,0 480,0 455,26 0,26" fill="url(#greyBand)"/>
      <polygon points="478,0 532,0 509,26 455,26 455,26" fill="var(--paper)" opacity="0"/>
      <polygon points="487,0 497,0 472,26 462,26" fill="var(--brand-red)"/>
      <polygon points="470,26 509,26 492,46 452,46" fill="var(--bright-red)"/>
      <polygon points="505,0 527,0 502,26 480,26" fill="var(--paper)"/>
      <polygon points="533,0 560,0 535,26 508,26" fill="#7d7d7d"/>
    </svg>
    <p class="reg-details">Reg. no: 5316274<span class="divider">|</span>VAT Reg. no: 5316274</p>
    <p class="registered-entity">Quorvix Ltd, Registered: England &amp; Wales</p>
  </footer>
</main>
</body>
</html>
```